Gobal construction supply company needs new business card design

I need a business card design for my global supply company using an existing logo. i will be looking to print these on rounded corner cards with the black background version of my logo on the back. on the front white background, my logo again and my simple details.

```html
<!DOCTYPE html>
<html lang="en">
<head>
<meta charset="utf-8">
<title>Meridian Build Supply — Business Card</title>
<link href="https://fonts.googleapis.com/css2?family=Roboto:wght@400;500;700&display=swap" rel="stylesheet">
<style>
  :root {
    --stage: #8f8d8b;
    --card-white: #f4f4f4;
    --card-black: #1c1c1c;
    --brand-red: #d90000;
    --ink: #111111;
    --paper-text: #ffffff;
  }
  * { margin: 0; padding: 0; box-sizing: border-box; }
  html, body {
    width: 1200px; height: 960px; overflow: hidden;
    background: var(--stage);
    font-family: "Roboto", Arial, sans-serif;
  }
  .canvas { position: relative; width: 1200px; height: 960px; }

  .card {
    position: absolute; width: 600px; height: 342px; border-radius: 22px;
  }
  .card--front { left: 314px; top: 113px; background: var(--card-white); }
  .card--back { left: 311px; top: 472px; background: var(--card-black); }

  .brand {
    position: absolute; left: 0; right: 0;
    display: flex; align-items: center; justify-content: center; gap: 12px;
  }
  .brand__dot {
    width: 22px; height: 22px; border-radius: 50%; background: var(--brand-red);
  }
  .brand__name {
    font-weight: 700; font-size: 22px; letter-spacing: 0.5px;
  }
  .card--front .brand { top: 112px; }
  .card--front .brand__name { color: var(--ink); }
  .card--back .brand { top: 156px; }
  .card--back .brand__name { color: var(--paper-text); font-size: 24px; }

  .details-panel {
    position: absolute; left: 30px; top: 189px; width: 540px; height: 133px;
    background: var(--brand-red); border-radius: 20px; color: var(--paper-text);
  }
  .contact-list {
    position: absolute; left: 36px; top: 21px; list-style: none;
    font-size: 15px; line-height: 19.2px;
  }
  .contact-list li { display: flex; align-items: center; gap: 9px; }
  .contact-list svg { width: 13px; height: 13px; fill: var(--ink); flex: none; }

  .person { position: absolute; left: 339px; top: 18px; }
  .person__name { font-weight: 700; font-size: 21px; color: var(--ink); line-height: 24px; }
  .person__role { font-weight: 500; font-size: 15px; line-height: 18px; }
  .person__address { margin-top: 17px; font-size: 15px; line-height: 18px; }
</style>
</head>
<body>
<main class="canvas">

  <section class="card card--front" aria-label="Card front">
    <div class="brand">
      <span class="brand__dot"></span>
      <span class="brand__name">MERIDIAN BUILD SUPPLY</span>
    </div>

    <div class="details-panel">
      <ul class="contact-list">
        <li>
          <svg viewBox="0 0 16 16" aria-hidden="true"><path d="M3.5 1l2.5 3-1.5 2c1 2 2.5 3.5 4.5 4.5l2-1.5 3 2.5-1.5 3C7 14 2 9 1 2.5z"/></svg>
          555 210 4471
        </li>
        <li>
          <svg viewBox="0 0 16 16" aria-hidden="true"><path d="M4 0h8a1 1 0 0 1 1 1v14a1 1 0 0 1-1 1H4a1 1 0 0 1-1-1V1a1 1 0 0 1 1-1zm1 2v10h6V2zm3 11a1 1 0 1 0 0 2 1 1 0 0 0 0-2z"/></svg>
          555 382 9016
        </li>
        <li>
          <svg viewBox="0 0 16 16" aria-hidden="true"><path d="M4 0h6l2 2v4H4zM1 7h14v7h-2v2H3v-2H1zm4 5v2h6v-2z"/></svg>
          555 647 2385
        </li>
        <li>
          <svg viewBox="0 0 16 16" aria-hidden="true"><path d="M0 3h16v1L8 9 0 4zm0 3l8 5 8-5v7H0z"/></svg>
          daniel@meridianbuild.com
        </li>
        <li>
          <svg viewBox="0 0 16 16" aria-hidden="true"><path d="M8 0a8 8 0 1 0 0 16A8 8 0 0 0 8 0zM3 4l3 1 1 3-2 2v3L2 9zm7-2l1 3-2 2 3 2 1 3 2-4-1-4z"/></svg>
          www.meridianbuild.com
        </li>
      </ul>

      <div class="person">
        <p class="person__name">DANIEL HARLOW</p>
        <p class="person__role">CEO/FOUNDER</p>
        <p class="person__address">1420 Cedar Ridge Road<br>Fairview, Oregon 97024</p>
      </div>
    </div>
  </section>

  <section class="card card--back" aria-label="Card back">
    <div class="brand">
      <span class="brand__dot"></span>
      <span class="brand__name">MERIDIAN BUILD SUPPLY</span>
    </div>
  </section>

</main>
</body>
</html>
```